Need a business card for our overland brand!

We had the logo made and we need a great design for our business card. Use the logo provide or tweak it however you see fit.

Contact Information for Business Card

Name, Title, Telephone, email, website

```html
<!DOCTYPE html>
<html lang="en">
<head>
<meta charset="utf-8">
<title>Ridge Roamers – Business Card</title>
<link href="https://fonts.googleapis.com/css2?family=Roboto:wght@400;700&display=swap" rel="stylesheet">
<style>
  :root {
    --navy: #263a52;
    --navy-soft: #2c4560;
    --glacier-blue: #1e9ec4;
    --ice: #e6f2f7;
    --paper: #ffffff;
    --ink: #2e2e33;
    --stage: #e9e6e1;
  }
  * { margin: 0; padding: 0; box-sizing: border-box; }
  html, body { width: 900px; height: 1200px; overflow: hidden; }
  body {
    background: var(--stage);
    font-family: "Roboto", Arial, sans-serif;
    position: relative;
  }
  .card {
    position: absolute;
    left: 105px;
    width: 692px;
    height: 403px;
    overflow: hidden;
    box-shadow: 0 4px 10px rgba(0,0,0,0.25);
  }
  .card--front { top: 155px; background: var(--paper); }
  .card--back { top: 640px; background: var(--navy); }

  .brand-name {
    position: absolute;
    font-weight: 700;
    text-transform: uppercase;
    line-height: 0.95;
    letter-spacing: 0.5px;
  }
  .card--front .brand-name {
    left: 46px; top: 80px;
    font-size: 60px;
    color: var(--navy);
  }
  .card--back .brand-name {
    left: 0; right: 0; top: 128px;
    text-align: center;
    font-size: 72px;
    color: var(--paper);
  }

  .range-art { position: absolute; left: 0; bottom: 0; width: 100%; }
  .card--front .range-art {
    height: 190px;
    background: linear-gradient(to bottom, rgba(255,255,255,0) 0%, var(--ice) 45%, var(--glacier-blue) 100%);
  }
  .card--back .range-art {
    height: 200px;
    background: linear-gradient(to bottom, rgba(44,69,96,0) 0%, var(--navy-soft) 100%);
  }

  .contact {
    position: absolute;
    right: 48px; top: 52px;
    text-align: right;
  }
  .contact__name {
    font-size: 26px; font-weight: 700;
    color: var(--navy); letter-spacing: 0.5px;
  }
  .contact__title {
    font-size: 18px; font-weight: 700;
    color: var(--glacier-blue); margin-top: 4px;
  }
  .contact__list { list-style: none; margin-top: 22px; }
  .contact__item {
    display: flex; justify-content: flex-end; align-items: center;
    gap: 9px;
    font-size: 20px; color: var(--ink);
    height: 34px;
  }
  .contact__icon {
    width: 19px; height: 19px;
    background: var(--glacier-blue);
    border-radius: 2px;
    display: flex; align-items: center; justify-content: center;
  }
  .contact__icon svg { width: 13px; height: 13px; }
</style>
</head>
<body>

<section class="card card--front">
  <div class="brand-name">Ridge<br>Roamers</div>

  <div class="contact">
    <div class="contact__name">NOLAN REYES</div>
    <div class="contact__title">CEO/FOUNDER</div>
    <ul class="contact__list">
      <li class="contact__item">555-013-2847
        <span class="contact__icon"><svg viewBox="0 0 16 16"><path fill="#fff" d="M3.5 1.5l2.5 0 1 3.5-1.8 1.2c.8 1.8 2.2 3.2 4 4l1.2-1.8 3.5 1v2.5c0 .8-.7 1.6-1.6 1.5C6.6 13 3 9.4 2 3.1 1.9 2.2 2.6 1.5 3.5 1.5z"/></svg></span>
      </li>
      <li class="contact__item">nolan@ridgeroamers.com
        <span class="contact__icon"><svg viewBox="0 0 16 16"><rect x="1.5" y="3.5" width="13" height="9" fill="none" stroke="#fff" stroke-width="1.4"/><path d="M1.5 3.5 8 9l6.5-5.5" fill="none" stroke="#fff" stroke-width="1.4"/></svg></span>
      </li>
      <li class="contact__item">www.ridgeroamers.com
        <span class="contact__icon"><svg viewBox="0 0 16 16" fill="none" stroke="#fff" stroke-width="1.2"><circle cx="8" cy="8" r="6"/><ellipse cx="8" cy="8" rx="2.6" ry="6"/><path d="M2 8h12M3 5h10M3 11h10"/></svg></span>
      </li>
    </ul>
  </div>

  <div class="range-art" role="img" aria-label="Wide mountain range illustration in glacier blue and white"></div>
</section>

<section class="card card--back">
  <div class="range-art" role="img" aria-label="Faint mountain range illustration in muted navy"></div>
  <div class="brand-name">Ridge<br>Roamers</div>
</section>

</body>
</html>
```